Business Card for premium dental clinic

We are a premium dental clinic based in Brasov, Romania with more than 15 year on the market, providing quality dental treatment made by a team of more specialized dentists, working with modern equipment as a solution to beautiful and healthy teeth.

Our current logo for the clinic use 2 square with colors black and gold - dr Corbescu - studio, using family fonts Bodoni, Myriad Pro and Segoe Print.
Depending on the printing we used some gold CMYK background or gold foil picture background or a gold gradient.
We want a business card:
- eye catching business card
- distinguished business card
- premium design
- to keep the color scheme of black and gold
- to attract the customers to spent time reading the information
- modern concept

```html
<!DOCTYPE html>
<html lang="en">
<head>
<meta charset="utf-8">
<title>Dr Corbescu Studio – Business Card</title>
<link rel="stylesheet" href="https://fonts.googleapis.com/css2?family=Roboto+Condensed:wght@300;400&family=Kalam:wght@400&display=swap">
<style>
  :root {
    --backdrop: #2e2822;
    --black: #000000;
    --white: #ffffff;
    --gold-light: #f6d862;
    --gold-mid: #e3b52a;
    --gold-deep: #b8860f;
    --gold-gradient: linear-gradient(135deg, var(--gold-light) 0%, var(--gold-mid) 35%, var(--gold-deep) 55%, var(--gold-mid) 75%, var(--gold-light) 100%);
  }
  * { box-sizing: border-box; margin: 0; padding: 0; }
  html, body { width: 900px; height: 1200px; overflow: hidden; }
  body {
    position: relative;
    background: var(--backdrop);
    font-family: "Roboto Condensed", "Arial Narrow", sans-serif;
    color: var(--white);
  }
  .card {
    position: absolute;
    left: 75px;
    width: 757px;
    background: var(--black);
    overflow: hidden;
  }
  .card--back { top: 128px; height: 442px; }
  .card--front { top: 632px; height: 443px; }

  .gold-foil {
    position: absolute;
    top: 0; left: 0; height: 100%;
    background: var(--gold-gradient);
  }
  .card--back .gold-foil { width: 305px; }
  .card--front .gold-foil { width: 366px; }

  .web-stripe {
    position: absolute;
    top: 0; left: 683px;
    width: 35px; height: 100%;
    background: var(--gold-gradient);
  }
  .web-stripe__text {
    position: absolute;
    top: 50%; left: 50%;
    transform: translate(-50%, -50%) rotate(90deg);
    white-space: nowrap;
    font-family: "Kalam", cursive;
    font-size: 20px;
    color: var(--black);
    letter-spacing: 0.5px;
  }

  .logo-frame {
    position: absolute;
    left: 52px; top: 44px;
    width: 506px; height: 248px;
    border: 2px solid var(--white);
  }

  .name-box {
    position: absolute;
    background: var(--white);
    color: var(--black);
    display: flex;
    align-items: center;
    justify-content: flex-end;
    font-weight: 300;
    white-space: nowrap;
  }
  .card--back .name-box { left: 83px; top: 127px; width: 222px; height: 85px; font-size: 36px; padding-right: 14px; }
  .card--front .name-box { left: 30px; top: 158px; width: 336px; height: 128px; font-size: 62px; padding-right: 22px; }

  .brand-word {
    position: absolute;
    font-weight: 300;
    color: var(--white);
    white-space: nowrap;
  }
  .card--back .brand-word { left: 348px; top: 150px; font-size: 40px; }
  .card--front .brand-word { left: 430px; top: 190px; font-size: 70px; }

  .descriptor {
    position: absolute;
    font-weight: 400;
    color: var(--white);
    white-space: nowrap;
  }
  .card--back .descriptor { left: 401px; top: 253px; font-size: 28px; }
  .card--front .descriptor { left: 512px; top: 350px; font-size: 42px; }

  .contact-list {
    position: absolute;
    left: 52px; top: 325px;
    list-style: none;
  }
  .contact-list li {
    display: flex;
    align-items: center;
    gap: 8px;
    height: 26px;
    font-size: 17px;
    color: var(--white);
  }
  .contact-list svg { width: 20px; height: 20px; flex: none; }

  .address {
    position: absolute;
    left: 322px; top: 325px;
    font-style: normal;
    font-size: 17px;
    line-height: 26px;
    letter-spacing: 0.3px;
  }
</style>
</head>
<body>

<section class="card card--back" aria-label="Business card back">
  <div class="gold-foil" role="img" aria-label="Crumpled gold foil texture"></div>
  <div class="logo-frame"></div>
  <div class="name-box">dr.Corbescu</div>
  <div class="brand-word">studio</div>
  <div class="descriptor">dental clinic</div>

  <ul class="contact-list">
    <li>
      <svg viewBox="0 0 20 20" aria-hidden="true"><circle cx="10" cy="10" r="9" fill="#e3b52a" stroke="#000" stroke-width="1.5"/><path d="M6.5 5.5l2 0 1 2.5-1.3 1a6 6 0 0 0 2.8 2.8l1-1.3 2.5 1v2a1 1 0 0 1-1 1A8 8 0 0 1 5.5 6.5a1 1 0 0 1 1-1z" fill="#000"/></svg>
      <span>268-410-3375</span>
    </li>
    <li>
      <svg viewBox="0 0 20 20" aria-hidden="true"><circle cx="10" cy="10" r="9" fill="#e3b52a" stroke="#000" stroke-width="1.5"/><rect x="5" y="6.5" width="10" height="7" fill="none" stroke="#000" stroke-width="1.4"/><path d="M5 6.5l5 4 5-4" fill="none" stroke="#000" stroke-width="1.4"/></svg>
      <span>268-410-3375</span>
    </li>
    <li>
      <svg viewBox="0 0 20 20" aria-hidden="true"><circle cx="10" cy="10" r="9" fill="#e3b52a" stroke="#000" stroke-width="1.5"/><rect x="7" y="5" width="6" height="3" fill="#000"/><rect x="5" y="8" width="10" height="5" rx="1" fill="#000"/><rect x="7" y="11.5" width="6" height="3.5" fill="#e3b52a" stroke="#000" stroke-width="1"/></svg>
      <span>Ana@corbescustudio.ro</span>
    </li>
  </ul>

  <address class="address">
    42 Republicii Street<br>
    Suite 3, Brasov<br>
    BV 500030
  </address>

  <div class="web-stripe" role="img" aria-label="Gold foil stripe">
    <span class="web-stripe__text">www.corbescustudio.com</span>
  </div>
</section>

<section class="card card--front" aria-label="Business card front">
  <div class="gold-foil" role="img" aria-label="Crumpled gold foil texture"></div>
  <div class="name-box">dr.Corbescu</div>
  <div class="brand-word">studio</div>
  <div class="descriptor">dental clinic</div>
</section>

</body>
</html>
```